Lend a Lantern Website Design (design layout only)

We need a website design for a new nonprofit organization based in Des Moines, Iowa called Lend a Lantern. The nonprofit provides soccer training opportunities to youth soccer players looking to improve their game while also affecting the lives of the less fortunate in a positive way. While participating in the training programs the players also go out and raise money for selected charities. The organization then donates the funds. In its first 18 months we donated $10,500. We would like to see designs attempt to symbolize the mission of the nonprofit - essentially "improve you while improving someone else."

We would like to see the following features:

· A place to donate - Our intent is to have the home page linked to the donation page; a simple straight-forward process for people to give money, and make donating as painless as possible - no account needed to make a donation, credit card or e-check should be the only information needed to donate, and have it be on a single page.

· A photo gallery so people can browse the photo gallery to get a better understanding of our organization and a place to add videos and a calendar to show upcoming events

· A place for contact information and the profiles of directors and board members. This should include a spot showing all the charities the organization donates to. Also includes a news section/blog for comments and suggestions.

We want the design to revolve around the content and mission. We would really like to stress our organization as nonprofit. We would also like if the website was user friendly and easy to navigate.

The logo of our organization is uploaded

```html
<!DOCTYPE html>
<html lang="en">
<head>
<meta charset="utf-8">
<title>Lend a Lantern</title>
<link href="https://fonts.googleapis.com/css2?family=Open+Sans:ital,wght@0,400;0,600;0,700;1,400;1,600&display=swap" rel="stylesheet">
<style>
:root{
  --green:#6f9a4d;
  --green-dark:#456d2c;
  --green-text:#4d7d31;
  --green-light:#8db466;
  --ink:#3a3a3a;
  --muted:#8a8a8a;
  --grey:#e6e6e6;
  --grey-mid:#cfcfcf;
  --footer:#1f1f1f;
  --footer-bar:#4f6e32;
  --white:#ffffff;
}
*{box-sizing:border-box;margin:0;padding:0}
html,body{width:687px;height:1200px;overflow:hidden}
body{position:relative;background:var(--white);font-family:'Open Sans',Arial,sans-serif;color:var(--ink)}
.abs{position:absolute}
p,h1,h2,h3,a{white-space:nowrap}

/* header */
.brand{left:80px;top:26px;width:90px;color:var(--green);font-weight:700;font-size:15px;line-height:16px;text-transform:uppercase;display:flex;align-items:flex-start;gap:5px}
.brand-mark{width:9px;height:9px;background:var(--green);margin-top:3px;flex:none}
.donate-tag{left:500px;top:10px;width:106px;height:16px;background:var(--green);color:var(--white);font-size:6.4px;font-weight:700;font-style:italic;display:flex;align-items:center;justify-content:center;transform:skewX(-15deg);white-space:nowrap}
.donate-tag span{transform:skewX(15deg)}
.nav{left:250px;top:45px;display:flex;font-size:7.2px;font-style:italic;color:#666;text-transform:uppercase}
.nav a{color:inherit;text-decoration:none;padding:0 8px;border-left:1px solid #ccc}
.nav a:first-child{border-left:0;padding-left:0;color:var(--green-dark)}
.search{left:589px;top:42px;width:18px;height:18px;border-radius:50%;background:var(--green)}

/* hero */
.hero{left:0;top:68px;width:687px;height:290px;background:linear-gradient(90deg,#dcdcdc,#efefef 40%,#e4e4e4);clip-path:polygon(0 4px,80px 26px,687px 8px,687px 286px,0 290px)}
.hero-photo{left:352px;top:76px;width:256px;height:256px;background:linear-gradient(90deg,rgba(160,160,160,0),#8a8a8a 22%,#5e5e5e 60%,#a9a9a9)}
.hero-title{left:74px;top:140px;font-size:24px;font-weight:700;color:#6a6a6a;letter-spacing:.3px}
.hero-sub{left:74px;top:171px;font-size:15px;font-weight:700;color:var(--green-text)}
.btn{background:var(--green);color:var(--white);font-weight:700;display:flex;align-items:center;justify-content:center;text-transform:uppercase}
.read-more{left:71px;top:222px;width:85px;height:23px;font-size:10px;color:#1f3512;border:1px solid var(--green-dark)}

/* donation panel */
.donated{left:78px;top:332px;width:166px;height:220px;background:var(--green);text-align:center}
.donated-intro{padding:12px 10px 0;font-size:8.6px;font-style:italic;color:var(--white);line-height:15px;white-space:normal}
.donated-label{margin-top:6px;font-size:26px;font-weight:700;color:var(--white);line-height:28px}
.donated-amount{font-size:34px;font-weight:700;color:#111;line-height:34px}
.donate-now{position:absolute;left:36px;top:126px;width:100px;height:24px;background:var(--white);color:var(--green-dark);font-size:10px;font-weight:700;display:flex;align-items:center;justify-content:center}
.donated-foot{position:absolute;left:0;top:139px;width:166px;height:81px;background:#333;color:var(--white);font-size:7.8px;font-weight:600;line-height:13px;padding-top:22px;white-space:nowrap}
.donated-foot b{display:block;font-size:15px;margin-top:5px}

/* welcome */
.welcome{left:244px;top:332px;width:364px;height:220px;background:var(--white);border-top:2px solid var(--green)}
.h2{font-size:13px;color:#666;text-transform:uppercase;font-weight:400}
.h2 b{color:var(--green-dark);font-weight:600}
.welcome-title{left:262px;top:344px}
.welcome-copy{left:262px;top:368px;width:334px;font-size:6.6px;line-height:11.7px;color:#777;white-space:normal}
.more-dot{display:inline-block;width:9px;height:9px;border-radius:50%;background:var(--green);vertical-align:middle;margin-left:3px}
.res-title{left:262px;top:440px;border-bottom:1px solid #ccc;padding-bottom:2px}
.res{width:120px;text-align:center;top:468px}
.res .circle{width:46px;height:46px;border-radius:50%;background:var(--grey-mid);margin:0 auto 6px;display:flex;align-items:center;justify-content:center}
.res .circle.on{background:var(--green)}
.res h3{font-size:10px;font-weight:400;color:var(--green-text)}
.res p{font-size:7px;color:#888;line-height:13px}

/* events */
.section-h{font-size:10.5px;color:#555;text-transform:uppercase;border-bottom:1px solid #ccc;padding-bottom:3px}
.section-h b{color:var(--green-dark);font-weight:600}
.event{top:594px;width:122px;height:74px;background:linear-gradient(135deg,#b09070,#6a5c4e)}
.event.e2{background:linear-gradient(135deg,#a09a90,#5f5a55)}
.event.e3{background:linear-gradient(135deg,#8a8a7a,#b0a090)}
.event-date{position:absolute;left:0;bottom:0;width:32px;height:44px;background:rgba(69,109,44,.9);color:var(--white);text-align:center;font-size:15px;line-height:18px;padding-top:5px}
.event-date small{display:block;font-size:6.5px;line-height:8px}
.event-cap{top:674px;font-size:8px;color:var(--green-text)}
.pager{left:452px;top:576px;font-size:10px;font-weight:700;color:#333;letter-spacing:3px}

.calendar{left:490px;top:577px;width:118px;height:107px;background:#f2f2f2}
.cal-head{height:19px;background:var(--green);color:var(--white);font-size:8px;font-weight:600;display:flex;align-items:center;justify-content:space-between;padding:0 5px}
.cal-days,.cal-grid{display:grid;grid-template-columns:repeat(7,1fr);gap:1px;padding:0 1px}
.cal-days{background:#ddd;font-size:5px;font-style:italic;text-align:center;line-height:11px;color:#444}
.cal-grid{margin-top:2px;row-gap:2px}
.cal-grid span{background:#dcdcdc;font-size:5.6px;text-align:center;line-height:13px;color:#333}
.cal-grid span.today{background:var(--green);color:var(--white)}

/* members */
.member{top:726px;width:121px;height:111px}
.member.m1{height:88px;background:linear-gradient(135deg,#e6e6e6,#9aa5b0)}
.member.m2{background:linear-gradient(135deg,#a07850,#e5b890)}
.member.m3{background:linear-gradient(135deg,#c9d2d8,#c8455a)}
.member.m4{background:linear-gradient(135deg,#dfe3e6,#34425a)}
.member-name{font-size:8px;color:#555}
.more-info{left:78px;top:842px;width:43px;height:14px;font-size:6.5px;font-weight:600;text-transform:none}

/* news */
.news-date{top:912px;font-size:8px;font-style:italic;color:var(--green-dark)}
.news-title{top:929px;font-size:8px;color:var(--green-text)}
.news-desc{top:942px;font-size:6.6px;line-height:10px;color:#888}
.more-news{left:78px;top:977px;width:48px;height:14px;font-size:6.5px;font-style:italic;font-weight:600;text-transform:none}
.divider{left:290px;top:888px;width:1px;height:104px;background:#ddd}
.gallery{left:304px;top:910px;display:grid;grid-template-columns:repeat(5,59px);grid-auto-rows:40px;gap:2px}
.gallery div{background:linear-gradient(135deg,#a87a55,#5a4a3e)}
.gallery div:nth-child(2){background:#222;display:flex;align-items:center;justify-content:center}
.gallery div:nth-child(3n){background:linear-gradient(135deg,#8b6f5a,#c08a6a)}
.gallery div:nth-child(4n){background:linear-gradient(135deg,#9a9488,#6b5a4a)}

/* footer */
.footer{left:0;top:1012px;width:687px;height:156px;background:var(--footer)}
.foot-h{font-size:8.6px;color:var(--green-light);text-transform:uppercase}
.review{left:78px;top:1026px;width:218px;height:126px;border:1px solid #4a5a3a}
.review-photo{left:91px;top:1050px;width:68px;height:68px;border-radius:50%;background:linear-gradient(160deg,#cfcfcf,#555);border:2px solid #666}
.review-text{left:165px;top:1055px;width:118px;font-size:7.6px;line-height:14px;color:#8e8e8e;white-space:normal}
.review-name{left:89px;top:1124px;font-size:7.2px;font-style:italic;color:var(--green-light)}
.review-sub{left:89px;top:1139px;font-size:6.4px;color:var(--green-light)}
.contact{left:332px;top:1038px;width:150px;font-size:6.6px;color:#bbb;line-height:9.5px}
.contact dt{color:var(--green-light);font-weight:600;margin-top:6px;font-size:6.4px}
.newsletter{left:488px;top:1012px;width:120px;height:140px;background:var(--green);text-align:center}
.newsletter h4{font-size:8.6px;font-weight:600;color:#1a1a1a;margin-top:13px}
.newsletter p{font-size:6px;line-height:8.5px;color:#1d2d12;margin:4px 12px 0;white-space:normal}
.email{position:absolute;left:8px;top:60px;width:104px;height:17px;background:var(--green-dark);border:1px solid #5a8440;font-size:6.4px;font-style:italic;color:#9bbd7d;text-align:left;padding:4px 6px}
.socials{left:489px;top:1107px;display:flex;gap:8px}
.socials span{width:18px;height:18px;background:#5d8440;border:1px solid #8db466}
.submit{left:488px;top:1131px;width:120px;height:21px;background:var(--green-light);color:#1a1a1a;font-size:9.5px;font-weight:600;display:flex;align-items:center;justify-content:center}
.bar{left:0;top:1168px;width:687px;height:32px;background:var(--footer-bar)}
.bar-links{left:78px;top:1179px;font-size:6.4px;color:var(--white)}
.bar-copy{right:79px;top:1179px;font-size:6.4px;color:#dfe8d5}
</style>
</head>
<body>

<header>
  <div class="abs brand"><span class="brand-mark"></span><span>Lend a<br>Lantern</span></div>
  <div class="abs donate-tag"><span>DONATE LEND A LANTERN</span></div>
  <nav class="abs nav">
    <a href="#">Home</a><a href="#">About us</a><a href="#">News</a><a href="#">Blogs</a><a href="#">Gallery</a><a href="#">Help</a><a href="#">Contact us</a>
  </nav>
  <div class="abs search">
    <svg width="18" height="18" viewBox="0 0 18 18"><circle cx="8" cy="8" r="3.5" fill="none" stroke="#fff" stroke-width="1.5"/><line x1="10.5" y1="10.5" x2="13" y2="13" stroke="#fff" stroke-width="1.5"/></svg>
  </div>
</header>

<section>
  <div class="abs hero" role="img" aria-label="Grey weathered wooden fence background"></div>
  <div class="abs hero-photo" role="img" aria-label="Black and white photo of two smiling children"></div>
  <h1 class="abs hero-title">IMPROVE YOU</h1>
  <p class="abs hero-sub">WHILE IMPROVING SOMEONE ELSE</p>
  <a class="abs btn read-more">Read more</a>
</section>

<section class="abs donated">
  <p class="donated-intro">The organization then Donates the funds. In its first 18 months we</p>
  <p class="donated-label">DONATED</p>
  <p class="donated-amount">$10,500</p>
  <div class="donated-foot">JOIN LEND A LANTERN ORGANIZATION!<br>DONATION SO FAR<b>$10,500</b></div>
  <a class="donate-now">DONATE NOW!</a>
</section>

<section class="abs welcome"></section>
<h2 class="abs h2 welcome-title">Welcome to <b>Lend a Lantern</b></h2>
<p class="abs welcome-copy">Lorem ipsum dolor sit amet, consectetur adipiscing elit. Ut pellentesque mi et vulputate tincdunt. Integer facilisis luctus magna, vitae dictum eros ullamcorper id. Duis non dignissim neque. Mauris pharetra odio nec ullamcorper dapibus. Praesent vitae erat non turpis veneatis mattis. Mauris enim justo, tempor ut euismod sed, feugiat ut augue. Morbi nec fermentum augue, eget tempor urna. Proin congue lectus sit amet dapibus tincidunt. <span class="more-dot"></span></p>
<h2 class="abs h2 res-title">Looking for <b>resources?</b></h2>
<div class="abs res" style="left:250px">
  <div class="circle on"><svg width="26" height="22" viewBox="0 0 26 22" fill="#fff"><circle cx="5" cy="4" r="3"/><circle cx="13" cy="4" r="3"/><circle cx="21" cy="4" r="3"/><path d="M2 9h6l1 7H7v6H4v-6H1zM10 9h6l1 7h-2v6h-3v-6H9zM18 9h6l1 7h-2v6h-3v-6h-3z"/></svg></div>
  <h3>Join Volunteer</h3><p>Lorem ipsum dolor sit amet,<br>consectetur adipiscing elit.</p>
</div>
<div class="abs res" style="left:374px">
  <div class="circle"><svg width="24" height="26" viewBox="0 0 24 26"><circle cx="12" cy="10" r="8" fill="#fff"/><path d="M6 20h12M12 18v4" stroke="#fff" stroke-width="2"/></svg></div>
  <h3>Education</h3><p>Lorem ipsum dolor sit amet,<br>consectetur adipiscing elit.</p>
</div>
<div class="abs res" style="left:499px">
  <div class="circle"><svg width="26" height="26" viewBox="0 0 26 26"><path d="M1 12a12 10 0 0 1 24 0z" fill="#fff"/><path d="M13 12v9a2 2 0 0 1-4 0" fill="none" stroke="#fff" stroke-width="1.5"/></svg></div>
  <h3>Help &amp; support</h3><p>Lorem ipsum dolor sit amet,<br>consectetur adipiscing elit.</p>
</div>

<h2 class="abs section-h" style="left:78px;top:570px">Upcomming <b>events</b></h2>
<div class="abs pager">&lsaquo;&rsaquo;</div>
<div class="abs event" style="left:78px" role="img" aria-label="Photo of a group of children"><div class="event-date">30<small>APR</small></div></div>
<div class="abs event e2" style="left:214px" role="img" aria-label="Photo of a person sleeping on the street"><div class="event-date">30<small>APR</small></div></div>
<div class="abs event e3" style="left:349px" role="img" aria-label="Photo of a village with laundry hanging"><div class="event-date">30<small>APR</small></div></div>
<p class="abs event-cap" style="left:78px">Lorem ipsum dolor sit amet</p>
<p class="abs event-cap" style="left:213px">Lorem ipsum dolor sit amet</p>
<p class="abs event-cap" style="left:348px">Lorem ipsum dolor sit amet</p>

<div class="abs calendar">
  <div class="cal-head"><span>&lsaquo;</span><span>JULY 2014</span><span>&rsaquo;</span></div>
  <div class="cal-days"><span>Sun</span><span>Mon</span><span>Tus</span><span>Wen</span><span>Thu</span><span>Fri</span><span>Sat</span></div>
  <div class="cal-grid">
    <span>01</span><span>02</span><span>03</span><span>04</span><span>05</span><span>06</span><span>07</span>
    <span>08</span><span>09</span><span>10</span><span>11</span><span>12</span><span>13</span><span>14</span>
    <span>15</span><span>16</span><span>17</span><span>18</span><span>19</span><span>20</span><span>21</span>
    <span>22</span><span>23</span><span>24</span><span class="today">25</span><span>26</span><span>27</span><span>28</span>
    <span>29</span><span>30</span><span>31</span><span>01</span><span>02</span><span>03</span><span>04</span>
  </div>
</div>

<h2 class="abs section-h" style="left:78px;top:702px">Our <b style="color:#555;font-weight:400">members</b></h2>
<div class="abs member m1" style="left:78px" role="img" aria-label="Photo of two women in a meeting"></div>
<div class="abs member m2" style="left:214px" role="img" aria-label="Photo of a couple reading on steps"></div>
<div class="abs member m3" style="left:351px" role="img" aria-label="Photo of a woman using a phone"></div>
<div class="abs member m4" style="left:487px" role="img" aria-label="Photo of a businesswoman smiling"></div>
<p class="abs member-name" style="left:78px;top:821px">Dr. Brick Jon</p>
<a class="abs btn more-info">More Info</a>
<p class="abs member-name" style="left:217px;top:842px">Dr. Lorem ispum</p>
<p class="abs member-name" style="left:354px;top:842px">Dr. Lorem ispum</p>
<p class="abs member-name" style="left:490px;top:842px">Dr. Lorem ispum</p>

<h2 class="abs section-h" style="left:78px;top:886px;width:88px">Latest <b>news</b></h2>
<p class="abs news-date" style="left:78px">20. 07. 2014</p>
<p class="abs news-title" style="left:78px">Lorem ipsum dolor sit</p>
<p class="abs news-desc" style="left:78px">Lorem ipsum dolor sit amet,<br>consectetur adipiscing elit</p>
<p class="abs news-date" style="left:187px">22. 07. 2014</p>
<p class="abs news-title" style="left:187px">Lorem ipsum dolor sit</p>
<p class="abs news-desc" style="left:187px">Lorem ipsum dolor sit amet,<br>consectetur adipiscing elit</p>
<a class="abs btn more-news">More News</a>
<div class="abs divider"></div>

<h2 class="abs section-h" style="left:302px;top:886px">Recent <b>videos &amp; photo</b></h2>
<div class="abs gallery" role="img" aria-label="Grid of photos of children and communities">
  <div></div>
  <div><svg width="24" height="24" viewBox="0 0 24 24"><circle cx="12" cy="12" r="10" fill="none" stroke="#fff" stroke-width="1.5"/><path d="M10 7.5l6 4.5-6 4.5z" fill="#fff"/></svg></div>
  <div></div><div></div><div></div><div></div><div></div><div></div><div></div><div></div>
</div>

<footer>
  <div class="abs footer"></div>
  <div class="abs review"></div>
  <h3 class="abs foot-h" style="left:78px;top:1023px;background:var(--footer);padding-right:4px">People reviews</h3>
  <div class="abs review-photo" role="img" aria-label="Portrait photo of a reviewer"></div>
  <p class="abs review-text">Lorem ipsum dolor sit amet, consectetur adipiscing elit. Mauris malesuada pulvinar eros, at suscipit turpis fermentum vitae.</p>
  <p class="abs review-name">Lorem ipsum dolor</p>
  <p class="abs review-sub">Consectetur site amet</p>

  <h3 class="abs foot-h" style="left:332px;top:1024px">Contact us</h3>
  <dl class="abs contact">
    <dt>ADDRESS</dt><dd>Lorem ipsum dolor 12453,. Dolor amet<br>Mauris malesuada pulvinar eros.</dd>
    <dt>PHONE NO</dt><dd>123 456 7890 &nbsp;/ &nbsp;0123 456 7899</dd>
    <dt>FAX NO</dt><dd>123 456 7890</dd>
    <dt>EMAIL ID</dt><dd>Lorem ipsum dolor 12453,. Dolor amet</dd>
  </dl>

  <div class="abs newsletter">
    <h4>SIGNUP NEWSLETTER</h4>
    <p>Quisque volutpat mattis eros. Nullamma lesuada erat ut turpis. Suspendisse.</p>
    <div class="email">Email</div>
  </div>
  <div class="abs socials"><span></span><span></span><span></span><span></span><span></span></div>
  <a class="abs submit">SUBMIT</a>

  <div class="abs bar"></div>
  <p class="abs bar-links">Home &nbsp;/&nbsp; About Us &nbsp;/&nbsp; News &nbsp;/&nbsp; Blogs &nbsp;/&nbsp; Gallery &nbsp;/&nbsp; Help &nbsp;/&nbsp; Contact Us</p>
  <p class="abs bar-copy">Copyright © 2013 LEND A LANTERN . All rights reserved</p>
</footer>

</body>
</html>
```